Dr. Plume Southern Reef Oil

We need a bottle label design for a new company called Dr. Plume. We sell krill oil in gel caps. Krill are shrimp-like crustaceans. We are looking for a professional concept that communicates the essence of ocean, health, life, purity...maybe a krill with medical authority.

There are a few labels out there. I attached 2. Dr. Halvorsen has some nice vector krill art, though the label is otherwise sparse. Copper Meadow has the feel of a nice full line of professional products, though there's nothing particularly krilly about it. Could there be a happy marriage of the two?

What we do NOT want is a photograph of an ocean with words over it. That screams Japanese karaoke.

Auxiliary wording on label front:
Heart Health
Antarctic
100% Pure
Dietary Supplements
1000mg

I apologize to designers for my new-to-crowd-design vagueness above, but I will try to be very forthcoming with feedback.

Thank you all!

Target Market(s)

Krill oil buyers. The 40+ crowd who want their Omega 3s and know that krill oil has it in spades!

Requirements
Nice to have
• A singular image that can be lifted for website branding as well...

```html
<!DOCTYPE html>
<html lang="en">
<head>
<meta charset="utf-8">
<title>Dr. Plume Southern Reef Oil – Bottle Label</title>
<link href="https://fonts.googleapis.com/css2?family=Roboto:wght@300;400;500;700&family=Roboto+Condensed:wght@400;700&display=swap" rel="stylesheet">
<style>
  :root {
    --navy: #1d3a73;
    --navy-dark: #142b5a;
    --ocean: #1f6fb6;
    --ocean-light: #3d93d2;
    --ink: #1e3766;
    --panel: #ffffff;
    --panel-line: #2a4a86;
    --ice-top: #c9d8e6;
    --ice-mid: #eef3f8;
    --ice-low: #dde8f1;
    --icon-red: #c8443a;
    --page: #eef2f6;
  }
  * { box-sizing: border-box; margin: 0; padding: 0; }
  html, body { width: 1200px; height: 1000px; overflow: hidden; }
  body {
    background: var(--page);
    font-family: "Roboto", Arial, sans-serif;
    color: var(--ink);
    position: relative;
  }
  .label {
    position: absolute;
    left: 30px; top: 310px;
    width: 1140px; height: 380px;
    overflow: hidden;
    box-shadow: 0 6px 24px rgba(20, 43, 90, .18);
  }
  .scenery {
    position: absolute; inset: 0;
    background: linear-gradient(180deg, var(--ice-top) 0%, var(--ice-mid) 45%, var(--ice-low) 80%, #cfe0ee 100%);
  }
  .top-band {
    position: absolute; left: 0; top: 0; width: 100%; height: 58px;
    background: var(--navy);
  }
  .bottom-band {
    position: absolute; left: 0; bottom: 0; width: 100%; height: 42px;
    background: linear-gradient(180deg, var(--ocean) 0%, var(--ocean-light) 55%, var(--ocean) 100%);
  }
  .brand-tab {
    position: absolute; left: 442px; top: 0; width: 256px; height: 78px;
    background: var(--navy);
    border-radius: 0 0 8px 8px;
    border-bottom: 3px solid #5f86c2;
    display: flex; align-items: center; justify-content: center; gap: 8px;
  }
  .brand-name {
    font-weight: 500; font-size: 44px; color: #fff; letter-spacing: -0.5px;
  }
  .brand-mark { width: 38px; height: 38px; background: #fff; border-radius: 4px; }
  .claim-tab {
    position: absolute; left: 442px; top: 322px; width: 256px; height: 58px;
    background: linear-gradient(180deg, var(--navy) 0%, var(--ocean) 100%);
    border-radius: 8px 8px 0 0;
    border-top: 3px solid #5f86c2;
    display: flex; align-items: flex-end; justify-content: center; padding-bottom: 14px;
    color: #fff; font-size: 16px; font-weight: 400; letter-spacing: .3px;
  }
  .product-title {
    position: absolute; left: 420px; top: 96px; width: 300px;
    text-align: center; font-family: "Roboto Condensed", Arial, sans-serif; font-weight: 700;
    color: var(--navy);
  }
  .product-line { font-size: 26px; line-height: 26px; letter-spacing: .2px; }
  .product-caps { font-size: 50px; line-height: 50px; border-bottom: 3px solid var(--navy); display: inline-block; padding: 0 2px; }
  .product-claim { font-size: 16px; line-height: 20px; margin-top: 2px; }
  .product-omega { font-size: 31px; line-height: 30px; text-align: right; padding-right: 18px; }
  .softgels {
    position: absolute; left: 495px; top: 224px; width: 165px; height: 64px;
    background: radial-gradient(ellipse at 50% 55%, rgba(217,154,28,.55) 0%, rgba(217,154,28,.15) 55%, rgba(217,154,28,0) 75%);
  }
  .pack-size {
    position: absolute; left: 420px; top: 290px; width: 300px; text-align: center;
    font-size: 14px; font-weight: 300; color: #34496e;
  }
  .benefit-icons {
    position: absolute; left: 500px; top: 314px; display: flex; gap: 16px;
    z-index: 2;
  }
  .panel {
    position: absolute; background: var(--panel);
    border: 1px solid var(--panel-line);
    box-shadow: 0 0 0 3px rgba(255,255,255,.8);
    color: var(--ink);
    font-size: 9.5px; line-height: 13px;
    padding: 0 8px;
    overflow: hidden;
  }
  .panel h2 {
    font-weight: 500; font-size: 16px; line-height: 20px; letter-spacing: 2.2px; text-align: center;
    color: var(--navy); padding: 9px 0 4px;
  }
  .panel .rule { border-top: 1px solid var(--panel-line); }
  .facts { left: 6px; top: 65px; width: 266px; height: 267px; white-space: nowrap; }
  .facts .row { display: flex; justify-content: space-between; padding: 1px 8px; }
  .facts table { width: 100%; border-collapse: collapse; table-layout: fixed; margin-top: 4px; }
  .facts td { padding: 0 0 1px 8px; }
  .facts td.amount { width: 68px; padding-left: 0; }
  .facts td.dv { width: 28px; padding-left: 0; }
  .facts .note { padding: 0 8px; }
  .facts .note.first { padding-top: 4px; }
  .facts .other { padding: 10px 8px 0; }
  .usage { left: 870px; top: 65px; width: 266px; height: 266px; }
  .usage p { padding: 0 8px; }
  .usage .dose { padding: 4px 8px 7px; }
  .usage .warn-head { padding-top: 3px; }
  .usage .gap { margin-top: 9px; }
  .usage .distributor {
    margin-top: 8px; padding: 6px 0 0; text-align: center; white-space: nowrap;
    font-size: 9px; border-top: 1px solid #d3dbe8;
  }
</style>
</head>
<body>
<main class="label">
  <div class="scenery" role="img" aria-label="Soft photograph of snowy Antarctic mountains and ice under a pale sky"></div>
  <div class="top-band"></div>
  <div class="bottom-band"></div>

  <header class="brand-tab">
    <span class="brand-name">Dr.Plume</span>
    <span class="brand-mark"></span>
  </header>

  <section class="product-title">
    <div class="product-line">SOUTHERN REEF</div>
    <div class="product-caps">OIL CAPS</div>
    <div class="product-claim">HEART HEALTH 100% PURE</div>
    <div class="product-omega">Omega-3</div>
  </section>

  <div class="softgels" role="img" aria-label="Photograph of golden oil softgel capsules"></div>
  <div class="pack-size">1000mg / 90 softgels</div>

  <div class="claim-tab">DIETARY SUPPLEMENTS</div>

  <div class="benefit-icons" aria-label="Benefits: heart, joints, brain, lungs">
    <svg width="24" height="24" viewBox="0 0 24 24"><circle cx="12" cy="12" r="11" fill="var(--icon-red)" stroke="#fff" stroke-width="1.5"/><path d="M12 17.5 6.8 12.4a3 3 0 0 1 4.4-4.2l.8.8.8-.8a3 3 0 0 1 4.4 4.2Z" fill="#fff"/></svg>
    <svg width="24" height="24" viewBox="0 0 24 24"><circle cx="12" cy="12" r="11" fill="#5f7fa6" stroke="#fff" stroke-width="1.5"/><path d="M12 5v5M12 14v5" stroke="#fff" stroke-width="2.4" stroke-linecap="round"/><circle cx="12" cy="12" r="1.6" fill="#fff"/></svg>
    <svg width="24" height="24" viewBox="0 0 24 24"><circle cx="12" cy="12" r="11" fill="var(--icon-red)" stroke="#fff" stroke-width="1.5"/><ellipse cx="12" cy="12" rx="6" ry="4.5" fill="none" stroke="#fff" stroke-width="1.6"/><path d="M12 7.5v9" stroke="#fff" stroke-width="1.2"/></svg>
    <svg width="24" height="24" viewBox="0 0 24 24"><circle cx="12" cy="12" r="11" fill="#b4574e" stroke="#fff" stroke-width="1.5"/><path d="M12 5v6M12 9l-3 2v6l2-1V11M12 9l3 2v6l-2-1V11" stroke="#fff" stroke-width="1.5" fill="none" stroke-linejoin="round"/></svg>
  </div>

  <section class="panel facts">
    <h2>SUPPLEMENT FACTS</h2>
    <div class="rule"></div>
    <div class="row"><span>Server Size: 2 softgels</span><span>Servings per container: 30</span></div>
    <div class="row"><span>Amount per Serving:</span><span>% DIV</span></div>
    <div class="rule"></div>
    <table>
      <tr><td>Vitamina A</td><td class="amount">100 IU</td><td class="dv">2%</td></tr>
      <tr><td>Nereid Reef Oil (NRO)</td><td class="amount">1,000mg</td><td class="dv">**</td></tr>
      <tr><td>Phospholipiods, omega-3 rich</td><td class="amount">400mg</td><td class="dv">**</td></tr>
      <tr><td>Eicosapentaenoic Acid (EPA)</td><td class="amount">150mg</td><td class="dv">**</td></tr>
      <tr><td>Docosahexaenoic Acid (DHA)</td><td class="amount">900mg</td><td class="dv">**</td></tr>
      <tr><td>Omega-6 fatty acids, total</td><td class="amount">20mg</td><td class="dv">**</td></tr>
      <tr><td><em>Transfa</em></td><td class="amount">0mg</td><td class="dv">**</td></tr>
      <tr><td>Astaxanthin</td><td class="amount">1.5mg</td><td class="dv">**</td></tr>
    </table>
    <div class="rule" style="margin-top:4px"></div>
    <p class="note first">*Percent Daily Values based on a 2,000 calorie diet</p>
    <p class="note">**Daily Value not established</p>
    <p class="other">Other ingredients: Gelatin (capsule), glycerin, &amp; water.<br>Expiration Date:</p>
  </section>

  <section class="panel usage">
    <h2>SUGGESTED USE</h2>
    <div class="rule"></div>
    <p class="dose">2 Softgels daily with the firs meal</p>
    <div class="rule"></div>
    <p class="warn-head">WARNING</p>
    <p>In at pretium augue. Phasellus porttitor gravida ultrices. Lorem ipsum dolor sit amet, consectetur adipiscing elit. Ut non sapien quis est eleifend</p>
    <p class="gap">Sed ut nisl eu odio dictum ullamcorper quis et urna. Nulla interdum vitae diam non rhoncus. Nam posuere vitae dui quis semper. In hac habitasse platea dictumst. Vestibulum pretium fermentum tellus vel auctor.</p>
    <p class="gap">Sed hendrerit commodo eros, non rhoncus enim accumsan id. Nulla imperdiet eu ligula a luctus. Nulla a lacus vel turpis euismod aliquet.</p>
    <p class="distributor">Distributed by: www.drplume.com / contact@drplume.com</p>
  </section>
</main>
</body>
</html>
```